PCとスマホデザインの両方納品をいただきますが、
まずはデザインイメージが確認しやすいPCページのみの提案をお願いします。
スマホページは当選者に納品時にお願いしたいと思います。
スマホサイズについて、カンバスサイズは横幅375pxで作成し、2倍の横幅750pxのサイズで書き出ししてください。
(Clarexディスプレイに対応するため)
スマホページ作成時は、メニューが展開した際のデザインもお願いします。
レスポンシブウェブデザインを意識したデザインでお願いします。

```html
<!DOCTYPE html>
<html lang="ja">
<head>
<meta charset="utf-8">
<title>有限会社北斗建装</title>
<link href="https://fonts.googleapis.com/css2?family=Noto+Sans+JP:wght@400;500;700&family=Noto+Serif+JP:wght@500;700;900&display=swap" rel="stylesheet">
<style>
:root{
  --blue:#1d4f9e;
  --navy:#153a75;
  --ink:#222;
  --muted:#666;
  --line:#d8d8d8;
  --pale:#f3f4f6;
  --white:#fff;
}
*{margin:0;padding:0;box-sizing:border-box}
html,body{width:1200px;height:4384px;overflow:hidden}
body{position:relative;background:var(--white);color:var(--ink);font-family:"Noto Sans JP",sans-serif;font-size:12px;line-height:1.9}
.serif{font-family:"Noto Serif JP",serif}
.abs{position:absolute}
.ph{position:absolute}
.site-header{position:absolute;left:0;top:0;width:1200px;height:64px;z-index:3}
.brand{position:absolute;left:16px;top:4px;background:var(--white);padding:4px 8px}
.brand small{display:block;font-size:8px;color:var(--muted);line-height:1.2}
.brand b{font-family:"Noto Serif JP",serif;font-size:26px;color:var(--blue);line-height:1.2}
.nav{position:absolute;right:160px;top:18px;display:flex;gap:22px;font-size:11px;font-weight:500}
.nav-cta{position:absolute;right:0;top:0;width:136px;height:64px;background:var(--navy);color:#fff;font-size:11px;display:flex;align-items:center;justify-content:center;gap:6px}
.hero{left:64px;top:20px;width:1136px;height:600px;background:linear-gradient(160deg,#c9ccd1,#8d939b 55%,#5d646e)}
.hero-copy{position:absolute;left:0;width:1200px;text-align:center;color:#fff;top:180px}
.hero-copy p{font-family:"Noto Serif JP",serif;font-size:18px;letter-spacing:.15em}
.hero-copy h1{font-family:"Noto Serif JP",serif;font-size:66px;font-weight:900;letter-spacing:.12em;line-height:1.5}
.block{background:var(--blue)}
.svc-title{font-family:"Noto Serif JP",serif;font-size:22px;font-weight:700;line-height:1.5}
.svc-text{font-size:11px;line-height:2;color:#333}
.svc-sub{font-size:12px;font-weight:700;margin-top:18px}
.badge{width:150px;height:44px;border:1px solid var(--line);background:var(--pale)}
.spec{font-size:10px;border-collapse:collapse}
.spec th,.spec td{padding:2px 18px 2px 0;text-align:left;font-weight:400}
.spec thead th{border-bottom:1px solid var(--ink);font-weight:700}
.tag{display:inline-block;background:var(--ink);color:#fff;font-size:10px;padding:2px 10px}
.eyebrow{font-size:9px;letter-spacing:.15em;font-weight:700}
.sec-h{font-family:"Noto Serif JP",serif;font-size:28px;font-weight:700;line-height:1.4}
.info{font-size:11px;border-collapse:collapse;width:420px}
.info th{width:110px;text-align:left;font-weight:500;vertical-align:top;padding:3px 0}
.info td{padding:3px 0;vertical-align:top}
.btn{display:flex;align-items:center;justify-content:center;color:#fff;background:var(--navy);font-size:11px}
.contact{left:0;top:3440px;width:1200px;height:680px;background:var(--pale)}
.field{position:absolute;left:340px;display:flex;align-items:center;gap:14px;font-size:10px}
.field label{width:120px}
.field .req{background:var(--navy);color:#fff;font-size:9px;padding:0 5px;margin-left:4px}
.field span.box{display:block;width:340px;height:28px;background:#fff;border:1px solid var(--line)}
.site-footer{left:0;top:4120px;width:1200px;height:264px;background:#fff;border-top:1px solid var(--line)}
.foot-col{font-size:10px;line-height:2.3}
</style>
</head>
<body>

<header class="site-header">
  <div class="brand"><small>建築工事・内装工事・耐火被覆工事</small><b>北斗</b></div>
  <nav class="nav"><span>ホーム</span><span>耐火被覆工事</span><span>フリーアクセスフロア</span><span>会社名由来</span><span>会社概要</span></nav>
  <div class="nav-cta"><svg width="12" height="10" viewBox="0 0 12 10"><rect x=".5" y=".5" width="11" height="9" fill="none" stroke="#fff"/><path d="M.5 .5l5.5 5 5.5-5" fill="none" stroke="#fff"/></svg>お問い合わせ</div>
</header>

<div class="ph hero" role="img" aria-label="鉄骨天井の下で高所作業台に乗り作業する職人の写真"></div>
<div class="hero-copy"><p>誇り、汗を流し続ける、未来を共に</p><h1>力・希望・確信</h1></div>

<section>
  <div class="abs block" style="left:140px;top:700px;width:460px;height:520px"></div>
  <div class="ph" style="left:210px;top:760px;width:360px;height:160px;background:linear-gradient(135deg,#6f7a86,#a4abb3)" role="img" aria-label="鉄骨梁に耐火被覆材を巻き付けた施工写真"></div>
  <div class="ph" style="left:210px;top:930px;width:175px;height:150px;background:linear-gradient(135deg,#9aa3ad,#d3d6da)" role="img" aria-label="天井際で作業する職人の写真"></div>
  <div class="ph" style="left:395px;top:930px;width:175px;height:150px;background:linear-gradient(135deg,#7d8790,#b8bec5)" role="img" aria-label="耐火被覆材の施工部分の写真"></div>
  <div class="ph" style="left:80px;top:1090px;width:305px;height:140px;background:linear-gradient(135deg,#b7bcc2,#e4e6e8)" role="img" aria-label="床面の施工状況の写真"></div>
  <div class="abs" style="left:630px;top:760px;width:440px">
    <h2 class="svc-title">耐火被覆工事（巻付け）</h2>
    <p class="svc-text" style="margin-top:16px">建物の鉄骨を火災の熱から守るため、耐火材を柱や梁に巻き付けて施工します。火災時に鉄骨の強度低下を防ぎ、建物の倒壊を遅らせることで人命と財産を守る重要な工事です。当社では現場の状況に合わせ、丁寧で確実な施工を心がけております。安全と品質を第一に、多くの現場で実績を重ねてまいりました。</p>
    <p class="svc-sub">使用材料</p>
    <p class="svc-text">耐火被覆材（巻付け工法）</p>
    <div class="badge" style="margin-top:6px"></div>
  </div>
</section>

<section>
  <div class="abs block" style="left:600px;top:1310px;width:490px;height:560px"></div>
  <div class="ph" style="left:630px;top:1280px;width:150px;height:140px;background:linear-gradient(135deg,#8a8f96,#c0c4c8)" role="img" aria-label="フロアパネル施工中の写真"></div>
  <div class="ph" style="left:790px;top:1280px;width:150px;height:140px;background:linear-gradient(135deg,#50565e,#8d939a)" role="img" aria-label="床下配線の写真"></div>
  <div class="ph" style="left:950px;top:1280px;width:150px;height:140px;background:linear-gradient(135deg,#9ea3a8,#d8dbde)" role="img" aria-label="完成したOAフロアの写真"></div>
  <div class="ph" style="left:630px;top:1430px;width:230px;height:200px;background:linear-gradient(135deg,#7e848b,#bfc3c7)" role="img" aria-label="通路のOAフロアの写真"></div>
  <div class="ph" style="left:870px;top:1430px;width:230px;height:200px;background:linear-gradient(135deg,#b4b59a,#dedfcc)" role="img" aria-label="タイルカーペット仕上げの写真"></div>
  <div class="ph" style="left:720px;top:1640px;width:300px;height:200px;background:linear-gradient(135deg,#70767d,#acb1b6)" role="img" aria-label="支持脚とパネルの写真"></div>
  <div class="abs" style="left:130px;top:1420px;width:430px">
    <h2 class="svc-title">フリーアクセスフロア<br>（OAフロア工事）</h2>
    <p class="svc-text" style="margin-top:16px">フリーアクセスフロアは、床下に配線スペースを設けるための二重床です。オフィスやサーバールームなどで、電源やLANケーブルを床下に収めることで、すっきりとした空間と安全な配線環境を実現します。レイアウト変更にも柔軟に対応できます。</p>
    <p class="svc-sub">本工事</p>
    <p class="svc-text">床の高さ、荷重条件、用途に合わせたパネルを選定し、下地の調整から仕上げまで一貫して施工いたします。</p>
    <p style="margin-top:16px"><span class="tag">取扱メーカー</span></p>
    <table class="spec" style="margin-top:8px">
      <thead><tr><th>OA フロア</th><th>工法</th><th>仕様</th><th>高さ(mm)</th></tr></thead>
      <tbody>
        <tr><td>Aメーカー</td><td>置敷き</td><td>樹脂</td><td>40〜</td></tr>
        <tr><td>Bメーカー</td><td>支持脚</td><td>スチール</td><td>50〜</td></tr>
        <tr><td>Cメーカー</td><td>支持脚</td><td>アルミ</td><td>100〜</td></tr>
        <tr><td>Dメーカー</td><td>置敷き</td><td>樹脂</td><td>50〜</td></tr>
        <tr><td>Eメーカー</td><td>支持脚</td><td>スチール</td><td>150〜</td></tr>
      </tbody>
    </table>
  </div>
</section>

<section>
  <div class="abs" style="left:0;top:1990px;width:1200px;text-align:center">
    <p class="eyebrow">ORIGIN OF COMPANY NAME</p>
    <h2 class="sec-h">会社名由来</h2>
  </div>
  <div class="ph" style="left:520px;top:2080px;width:160px;height:220px;background:radial-gradient(circle at 50% 45%,#c8c8c8,#f4f4f4 70%)" role="img" aria-label="馬上の武将の墨絵風イラスト"></div>
  <p class="abs svc-text" style="left:200px;top:2330px;width:800px">北斗（ほくと）は、古くから旅人の道しるべとして夜空に輝く北斗七星に由来します。どんな時代でも変わらず進むべき方向を示し続ける星のように、お客様にとって信頼できる存在でありたいという想いを込めました。職人一人ひとりが誇りを持ち、確かな技術で現場に向き合うこと。そして地域とともに成長し、次の世代へと技術をつないでいくこと。その決意を社名に刻み、私たちは日々の仕事に取り組んでおります。</p>
</section>

<section>
  <div class="abs block" style="left:40px;top:2680px;width:640px;height:700px"></div>
  <div class="abs" style="left:70px;top:2640px;width:540px;height:700px;background:#fff;padding:30px 40px">
    <p class="eyebrow">COMPANY</p>
    <h2 class="sec-h" style="margin-bottom:18px">会社概要</h2>
    <table class="info">
      <tr><th>会社名</th><td>有限会社北斗建装</td></tr>
      <tr><th>住所</th><td>〒000-0000<br>東京都架空区サンプル町1-2-3<br>フリーダイヤル 0120-000-000</td></tr>
      <tr><th>設立</th><td>平成10年4月</td></tr>
      <tr><th>資本金</th><td>300万円</td></tr>
      <tr><th>代表</th><td>代表取締役 北斗 太郎</td></tr>
      <tr><th>事業内容</th><td>耐火被覆工事・内装工事<br>フリーアクセスフロア工事</td></tr>
      <tr><th>主な施工実績</th><td>大型物流倉庫<br>商業施設<br>オフィスビル<br>工場・研究施設<br>病院・福祉施設<br>学校・公共施設<br>集合住宅</td></tr>
      <tr><th>主要取引先</th><td>株式会社サンプル建設<br>株式会社テスト工業<br>架空建設株式会社</td></tr>
    </table>
    <div class="ph" style="left:40px;top:560px;width:200px;height:100px;background:linear-gradient(135deg,#9aa0a8,#d0d3d7)" role="img" aria-label="社員の集合写真"></div>
  </div>
  <div class="ph" style="left:720px;top:2690px;width:420px;height:380px;background:linear-gradient(135deg,#e6e8ea,#f5f5f3)" role="img" aria-label="会社所在地周辺の地図"></div>
  <svg class="abs" style="left:920px;top:2845px" width="22" height="30" viewBox="0 0 22 30"><path d="M11 0C5 0 0 5 0 11c0 8 11 19 11 19s11-11 11-19C22 5 17 0 11 0z" fill="#d93025"/><circle cx="11" cy="11" r="4" fill="#fff"/></svg>
  <div class="abs btn" style="left:860px;top:3100px;width:140px;height:34px">地図を見る</div>
</section>

<section class="abs contact">
  <div style="position:absolute;top:50px;width:1200px;text-align:center">
    <p class="eyebrow">CONTACT US</p>
    <h2 class="sec-h">お問い合わせ</h2>
    <p style="font-size:10px;margin-top:10px;color:var(--muted)">下記フォームよりお気軽にお問い合わせください。<br>担当者より折り返しご連絡いたします。</p>
  </div>
  <div class="field" style="top:200px"><label>お問い合わせ項目<span class="req">必須</span></label><span class="box"></span></div>
  <div class="field" style="top:245px"><label>会社名</label><span class="box"></span></div>
  <div class="field" style="top:290px"><label>お名前<span class="req">必須</span></label><span class="box"></span></div>
  <div class="field" style="top:335px"><label>フリガナ<span class="req">必須</span></label><span class="box"></span></div>
  <div class="field" style="top:380px"><label>電話番号<span class="req">必須</span></label><span class="box"></span></div>
  <div class="field" style="top:425px"><label>メールアドレス<span class="req">必須</span></label><span class="box"></span></div>
  <div class="field" style="top:470px;align-items:flex-start"><label>お問い合わせ内容<span class="req">必須</span></label><span class="box" style="height:90px"></span></div>
  <div class="abs btn" style="left:520px;top:600px;width:200px;height:36px">お問い合わせを送信</div>
</section>

<footer class="abs site-footer">
  <div class="abs" style="left:40px;top:40px">
    <b class="serif" style="font-size:32px;color:var(--blue)">北斗</b>
  </div>
  <div class="abs foot-col" style="left:130px;top:40px">
    建築工事・内装工事・耐火被覆工事<br><b style="font-size:14px">有限会社北斗建装</b><br>〒000-0000 東京都架空区サンプル町1-2-3<br>
    <svg width="60" height="12" viewBox="0 0 60 12"><circle cx="6" cy="6" r="6" fill="#222"/><circle cx="26" cy="6" r="6" fill="#222"/><circle cx="46" cy="6" r="6" fill="#222"/></svg>
  </div>
  <div class="abs foot-col" style="left:480px;top:36px">ホーム<br>耐火被覆工事<br>フリーアクセスフロア<br>会社名由来<br>会社概要</div>
  <div class="abs foot-col" style="left:640px;top:36px">お問い合わせ<br>採用情報<br>プライバシーポリシー</div>
  <div class="abs" style="left:900px;top:40px;text-align:left">
    <p style="font-size:10px">お電話でのお問い合わせ</p>
    <p style="font-size:9px;color:var(--muted)">受付時間 平日 9:00〜18:00</p>
    <p style="font-size:32px;font-weight:700;color:var(--navy);line-height:1.3">000-0000-0000</p>
  </div>
  <p class="abs" style="left:40px;top:220px;font-size:9px;color:var(--muted)">© 有限会社北斗建装 All Rights Reserved.</p>
</footer>

</body>
</html>
```